Dachfund Flyer

We need a flyer (one-sided) that is printed on both sides for our service in Cologne, Germany. We would like to offer people the opportunity to sell unused items from your house that are in the basement or in the attic.
The service is called "Dachfund"
We:
1) take photos
2) try to sell the items (for a pre-defined amount)
3) the customer receives 70% of the proceeds
What could be items (at least 50 €):
- clocks
- Furniture
- Jewellery
- Etc
Use:
- Make space for something new in your home
- get rid of your junk
- Make a substantial amount of money with unused items
This service is non-binding, risk-free and free of charge until it is sold.
Customers can contact me via ChatPost on 0152 81730254 and send pictures or descriptions.
Target Market(s)
Wealthy households
Logo Text
Dachfund
Requirements
Must have
- Note:
Dachfund cannot guarantee a sale
High quality and serious appearance - it should almost be like an invitation

```html
<!DOCTYPE html>
<html lang="en">
<head>
<meta charset="utf-8">
<title>Dachfund Flyer</title>
<link href="https://fonts.googleapis.com/css2?family=Roboto+Condensed:wght@700&family=Raleway:wght@300;400;500;600;700;800&display=swap" rel="stylesheet">
<style>
  :root {
    --navy: #0c2c46;
    --navy-deep: #08223a;
    --cyan: #2bc3ef;
    --teal-soft: #7fb8c4;
    --band: #eef8fb;
    --ink: #1d2a36;
    --white: #ffffff;
    --stage: #dcd8d3;
  }
  * { box-sizing: border-box; margin: 0; padding: 0; }
  html, body { width: 1200px; height: 1200px; overflow: hidden; background: var(--stage); }
  body { font-family: "Raleway", sans-serif; color: var(--ink); position: relative; }

  .flyer {
    position: absolute; left: 156px; top: 30px;
    width: 888px; height: 1140px;
    background: var(--white);
    box-shadow: 0 6px 22px rgba(0,0,0,0.18);
    overflow: hidden;
  }

  /* Hero */
  .hero {
    position: absolute; left: 0; top: 0; width: 888px; height: 586px;
    background: radial-gradient(ellipse at 70% 40%, #123a58 0%, var(--navy) 55%, var(--navy-deep) 100%);
  }
  .headline {
    position: absolute; left: 58px; top: 64px;
    font-family: "Roboto Condensed", sans-serif; font-weight: 700;
    font-size: 61px; line-height: 68px; letter-spacing: 0.2px;
    color: var(--white); text-transform: uppercase;
  }
  .headline .accent {
    background: linear-gradient(90deg, var(--teal-soft) 0%, var(--cyan) 100%);
    -webkit-background-clip: text; background-clip: text; color: transparent;
    display: inline-block;
  }
  .hero-sub {
    position: absolute; left: 58px; top: 336px; width: 460px;
    font-weight: 300; font-size: 21px; line-height: 27px; color: var(--cyan);
  }
  .brand-dash { position: absolute; left: 58px; top: 462px; width: 44px; height: 3px; background: var(--cyan); }
  .brand-name {
    position: absolute; left: 56px; top: 480px;
    font-weight: 800; font-size: 50px; letter-spacing: 0.5px; color: var(--cyan);
  }
  .hero-photo {
    position: absolute; left: 532px; top: 60px; width: 313px; height: 526px;
    border-radius: 150px 150px 0 0;
    background: linear-gradient(180deg, #8a5a3c 0%, #e8795a 45%, #f1f0ee 80%, #e2e2e0 100%);
    opacity: 0.92;
  }

  /* Process band */
  .process { position: absolute; left: 0; top: 586px; width: 888px; height: 167px; background: var(--band); }
  .process-label {
    position: absolute; left: 56px; top: 26px;
    font-weight: 800; font-size: 26px; color: var(--navy);
  }
  .process-label::after {
    content: ""; position: absolute; left: 0; top: 40px; width: 30px; height: 3px; background: var(--cyan);
  }
  .step { position: absolute; top: 30px; width: 240px; text-align: center; }
  .step svg { display: block; margin: 0 auto; }
  .step p { margin-top: 12px; font-size: 16.5px; line-height: 20px; color: var(--ink); }
  .step-photos { left: 114px; }
  .step-sell { left: 337px; }
  .step-receive { left: 631px; }
  .step-arrow { position: absolute; top: 60px; }
  .arrow-one { left: 333px; }
  .arrow-two { left: 600px; }

  /* Lower content */
  .section-title {
    position: absolute; font-weight: 800; font-size: 27px; line-height: 38px; color: var(--navy);
  }
  .items-title { left: 56px; top: 780px; }
  .items-title .min { font-weight: 500; }
  .items-title .amount { color: var(--cyan); font-weight: 800; font-size: 32px; }
  .title-rule { position: absolute; left: 56px; top: 867px; width: 44px; height: 3px; background: var(--cyan); }

  .item { position: absolute; top: 898px; width: 120px; text-align: center; }
  .item svg { display: block; margin: 0 auto; }
  .item p { margin-top: 10px; font-size: 16px; color: var(--ink); }
  .item-clocks { left: 29px; }
  .item-furniture { left: 158px; }
  .item-jewellery { left: 294px; }
  .item-etc { left: 413px; }

  .column-divider {
    position: absolute; left: 546px; top: 774px; width: 1px; height: 234px;
    background: #e3e7ea; box-shadow: -3px 0 8px rgba(0,0,0,0.06);
  }
  .use-title { left: 597px; top: 782px; }
  .benefits { position: absolute; left: 597px; top: 846px; width: 270px; list-style: none; }
  .benefits li { position: relative; padding-left: 20px; font-size: 17px; line-height: 20px; color: var(--ink); }
  .benefits li + li { margin-top: 22px; }
  .benefits li:nth-child(3) { margin-top: 23px; }
  .benefits svg { position: absolute; left: 0; top: 3px; }

  .terms-bar {
    position: absolute; left: 46px; top: 1026px; width: 795px; height: 39px;
    background: var(--navy); color: var(--white);
    font-weight: 600; font-size: 21.5px; line-height: 39px; text-align: center;
  }
  .terms-bar em, .contact em { font-style: normal; color: var(--cyan); }
  .contact {
    position: absolute; left: 0; top: 1083px; width: 888px; text-align: center;
    font-weight: 600; font-size: 16px; color: #111;
  }
  .contact em { font-weight: 500; }
  .disclaimer {
    position: absolute; right: 41px; top: 1110px; font-size: 10px; font-weight: 500; color: #333;
  }
  .footer-strip { position: absolute; left: 0; top: 1128px; width: 888px; height: 12px; background: var(--cyan); }
</style>
</head>
<body>
<main class="flyer">

  <section class="hero">
    <h1 class="headline">
      <span class="accent">The</span><br>
      <span class="accent">Opportunity</span><br>
      To Sell<br>
      Unused Items
    </h1>
    <p class="hero-sub">from your house that are in the basement or in the attic.</p>
    <div class="brand-dash"></div>
    <div class="brand-name">DACHFUND</div>
    <div class="hero-photo" role="img" aria-label="Photo of a smiling woman in an orange sweater holding a stack of white boxes"></div>
  </section>

  <section class="process">
    <h2 class="process-label">WE</h2>

    <div class="step step-photos">
      <svg width="58" height="44" viewBox="0 0 58 44" aria-hidden="true">
        <rect x="2" y="8" width="54" height="34" rx="4" fill="var(--cyan)"/>
        <rect x="18" y="2" width="20" height="10" rx="2" fill="var(--cyan)"/>
        <rect x="7" y="4" width="7" height="5" rx="1" fill="var(--cyan)"/>
        <circle cx="30" cy="25" r="11" fill="var(--white)"/>
        <circle cx="30" cy="25" r="7.5" fill="var(--cyan)"/>
        <rect x="8" y="13" width="6" height="3" fill="var(--white)"/>
      </svg>
      <p>Take photos</p>
    </div>

    <svg class="step-arrow arrow-one" width="26" height="18" viewBox="0 0 26 18" aria-hidden="true">
      <path d="M2 9H23M15 2l8 7-8 7" fill="none" stroke="var(--cyan)" stroke-width="2.5"/>
    </svg>

    <div class="step step-sell">
      <svg width="62" height="56" viewBox="0 0 62 56" aria-hidden="true">
        <path d="M2 4h8l2 6h46l-8 26H16L10 10" fill="none" stroke="var(--cyan)" stroke-width="4" stroke-linejoin="round"/>
        <path d="M13 10h45l-8 26H18z" fill="var(--cyan)"/>
        <path d="M35 32V18M28 24l7-7 7 7" fill="none" stroke="var(--white)" stroke-width="3.5"/>
        <circle cx="22" cy="48" r="4" fill="var(--cyan)"/>
        <circle cx="46" cy="48" r="4" fill="var(--cyan)"/>
      </svg>
      <p>Try to sell the items<br>(for a pre-defined amount)</p>
    </div>

    <svg class="step-arrow arrow-two" width="26" height="18" viewBox="0 0 26 18" aria-hidden="true">
      <path d="M2 9H23M15 2l8 7-8 7" fill="none" stroke="var(--cyan)" stroke-width="2.5"/>
    </svg>

    <div class="step step-receive">
      <svg width="62" height="58" viewBox="0 0 62 58" aria-hidden="true">
        <circle cx="12" cy="7" r="6" fill="var(--cyan)"/>
        <path d="M4 16h16v20h-3v20h-4V38h-2v18H7V36H4z" fill="var(--cyan)"/>
        <path d="M46 2v16M40 12l6 7 6-7" fill="none" stroke="var(--cyan)" stroke-width="3"/>
        <rect x="30" y="26" width="30" height="28" fill="var(--cyan)"/>
        <path d="M40 26v10h10V26" fill="var(--white)"/>
      </svg>
      <p>The customer receives<br>70% of the proceeds</p>
    </div>
  </section>

  <h2 class="section-title items-title">WHAT COULD BE ITEMS<br><span class="min">( AT LEAST <span class="amount">50€</span> )</span></h2>
  <div class="title-rule"></div>

  <div class="item item-clocks">
    <svg width="52" height="52" viewBox="0 0 52 52" aria-hidden="true">
      <circle cx="26" cy="26" r="23" fill="none" stroke="var(--cyan)" stroke-width="2.5"/>
      <circle cx="26" cy="26" r="18" fill="none" stroke="var(--cyan)" stroke-width="1.5"/>
      <path d="M26 13v13l9 6" fill="none" stroke="var(--cyan)" stroke-width="2"/>
    </svg>
    <p>Clocks</p>
  </div>

  <div class="item item-furniture">
    <svg width="60" height="52" viewBox="0 0 60 52" aria-hidden="true">
      <g fill="none" stroke="var(--cyan)" stroke-width="2.2" stroke-linejoin="round">
        <path d="M10 22V12c0-4 3-6 7-6h26c4 0 7 2 7 6v10"/>
        <path d="M4 22c0-3 2-5 5-5s5 2 5 5v8h32v-8c0-3 2-5 5-5s5 2 5 5v14H4z"/>
        <path d="M8 36v6M52 36v6"/>
      </g>
    </svg>
    <p>Furniture</p>
  </div>

  <div class="item item-jewellery">
    <svg width="44" height="54" viewBox="0 0 44 54" aria-hidden="true">
      <g fill="none" stroke="var(--cyan)" stroke-width="2.5" stroke-linejoin="round">
        <path d="M15 3h14l5 7-12 10L10 10z"/>
        <circle cx="22" cy="35" r="15"/>
        <circle cx="22" cy="35" r="9"/>
      </g>
    </svg>
    <p>Jewellery</p>
  </div>

  <div class="item item-etc">
    <svg width="54" height="52" viewBox="0 0 54 52" aria-hidden="true">
      <g fill="none" stroke="var(--cyan)" stroke-width="2" stroke-linejoin="round">
        <path d="M4 16l22-10 24 8v24L28 48 4 40z"/>
        <path d="M4 16l24 8 22-10M28 24v24"/>
        <path d="M14 11l24 8v8"/>
        <rect x="9" y="32" width="10" height="6"/>
      </g>
    </svg>
    <p>Etc</p>
  </div>

  <div class="column-divider"></div>

  <h2 class="section-title use-title">USE:</h2>
  <ul class="benefits">
    <li><svg width="14" height="14" viewBox="0 0 14 14" aria-hidden="true"><rect x="1" y="2" width="11" height="11" fill="none" stroke="var(--cyan)" stroke-width="1.3"/><path d="M3.5 7l3 3 6-8" fill="none" stroke="var(--cyan)" stroke-width="1.5"/></svg>Make space for something new in your home</li>
    <li><svg width="14" height="14" viewBox="0 0 14 14" aria-hidden="true"><rect x="1" y="2" width="11" height="11" fill="none" stroke="var(--cyan)" stroke-width="1.3"/><path d="M3.5 7l3 3 6-8" fill="none" stroke="var(--cyan)" stroke-width="1.5"/></svg>Get rid of your junk</li>
    <li><svg width="14" height="14" viewBox="0 0 14 14" aria-hidden="true"><rect x="1" y="2" width="11" height="11" fill="none" stroke="var(--cyan)" stroke-width="1.3"/><path d="M3.5 7l3 3 6-8" fill="none" stroke="var(--cyan)" stroke-width="1.5"/></svg>Make a substantial amount of money with unused items</li>
  </ul>

  <p class="terms-bar">This service is <em>non-binding, risk-free</em> and <em>free of charge</em> until it is sold.</p>
  <p class="contact">Customers can contact me via <em>ChatPost on 0152 81730254</em> and send pictures or descriptions.</p>
  <p class="disclaimer">*Dachfund cannot guarantee a sale</p>
  <div class="footer-strip"></div>

</main>
</body>
</html>
```